AWESOME CYBER MONDAY SALE AD NEEDED

Create a Cyber Monday ad for nitrile gloves. We are offering a box of 100, no-powder, exam grade nitrile gloves, for $9.99. No limit. Each case is $99. Create something simple, eye catching, cool. KelpTorch.com. Sale ends on December 4th. While supplies last. We are a local medical supply company in Hawaii that serves the general public in addition to local businesses, government, etc. Gloves are in short supply and we have tons of inventory ready to sell.

Target Market(s)

Businesses that use supplies such as gloves

Industry/Entity Type

medical supplies

Requirements
Must have
• The company logo, website, picture of gloves and pricing.

```html
<!DOCTYPE html>
<html lang="en">
<head>
<meta charset="utf-8">
<title>Cyber Monday Sale – KelpTorch.com</title>
<link href="https://fonts.googleapis.com/css2?family=Quicksand:wght@500;600&family=Arimo:wght@400;700&display=swap" rel="stylesheet">
<style>
  :root {
    --page: #ffffff;
    --panel: #000000;
    --neon-pink: #f03cf5;
    --neon-cyan: #19f3f7;
    --neon-white: #ffffff;
    --lime: #22f01a;
    --glove-light: #7ec2f0;
    --glove-mid: #4a9ee0;
    --glove-dark: #2f7cc2;
    --ink: #000000;
    --text: #ffffff;
  }
  * { margin: 0; padding: 0; box-sizing: border-box; }
  html, body { width: 1200px; height: 1000px; overflow: hidden; background: var(--page); }
  .canvas { position: relative; width: 1200px; height: 1000px; }
  .ad {
    position: absolute; left: 195px; top: 95px; width: 810px; height: 810px;
    background: var(--panel); overflow: hidden;
  }
  .glove-photo {
    position: absolute; left: 60px; top: 148px; width: 390px; height: 455px;
    background: radial-gradient(ellipse at 45% 45%, var(--glove-light) 0%, var(--glove-mid) 45%, var(--glove-dark) 70%, rgba(0,0,0,0) 78%);
    border-radius: 45% 45% 40% 40%;
  }
  .headline { position: absolute; font-family: "Quicksand", sans-serif; font-weight: 600; line-height: 1; white-space: nowrap; }
  .headline--cyber {
    left: 152px; top: 28px; font-size: 128px; color: var(--neon-pink);
    text-shadow: 0 0 10px var(--neon-pink), 0 0 26px var(--neon-pink);
  }
  .headline--monday {
    left: 298px; top: 142px; font-size: 124px; color: var(--neon-cyan);
    text-shadow: 0 0 10px var(--neon-cyan), 0 0 26px var(--neon-cyan);
  }
  .headline--sale {
    left: 483px; top: 253px; font-size: 106px; color: var(--neon-white);
    text-shadow: 0 0 8px rgba(255,255,255,.8), 0 0 22px rgba(255,255,255,.6);
  }
  .offer { position: absolute; left: 380px; top: 370px; width: 410px; text-align: center; font-family: "Arimo", sans-serif; color: var(--text); }
  .offer__title { font-size: 28px; letter-spacing: .3px; }
  .offer__list { list-style: none; margin-top: 10px; }
  .offer__item { font-size: 21px; line-height: 34px; display: flex; justify-content: center; align-items: center; gap: 12px; }
  .offer__tick { width: 20px; height: 20px; flex: none; }
  .price { position: absolute; left: 428px; top: 497px; font-family: "Arimo", sans-serif; font-weight: 700; color: var(--lime); }
  .price__for { position: absolute; left: 2px; top: 0; font-size: 30px; }
  .price__main { position: absolute; left: 0; top: 8px; font-size: 166px; letter-spacing: -6px; line-height: 1; white-space: nowrap; }
  .price__cents { position: absolute; left: 222px; top: 18px; font-size: 92px; letter-spacing: -3px; line-height: 1; }
  .case-note {
    position: absolute; left: 427px; top: 665px; width: 316px; height: 33px;
    background: var(--lime); color: var(--ink); font-family: "Arimo", sans-serif; font-weight: 700;
    font-size: 20px; line-height: 33px; text-align: center;
  }
  .closing { position: absolute; left: 380px; top: 724px; width: 410px; text-align: center; font-family: "Arimo", sans-serif; font-weight: 700; font-size: 20px; line-height: 30px; color: var(--text); }
  .closing__url { color: var(--lime); }
  .brand { position: absolute; left: 68px; top: 720px; font-family: "Arimo", sans-serif; font-weight: 700; font-size: 50px; color: var(--text); letter-spacing: -1px; }
</style>
</head>
<body>
<div class="canvas">
  <section class="ad">
    <div class="glove-photo" role="img" aria-label="Pair of blue nitrile exam gloves"></div>

    <div class="headline headline--cyber">Cyber</div>
    <div class="headline headline--monday">Monday</div>
    <div class="headline headline--sale">Sale</div>

    <div class="offer">
      <p class="offer__title">A BOX OF 100 PIECES</p>
      <ul class="offer__list">
        <li class="offer__item"><svg class="offer__tick" viewBox="0 0 20 20"><path d="M2 11 L8 17 L18 3" fill="none" stroke="#22f01a" stroke-width="3.5" stroke-linecap="round" stroke-linejoin="round"/></svg>POWDER-FREE GLOVES</li>
        <li class="offer__item"><svg class="offer__tick" viewBox="0 0 20 20"><path d="M2 11 L8 17 L18 3" fill="none" stroke="#22f01a" stroke-width="3.5" stroke-linecap="round" stroke-linejoin="round"/></svg>EXAM GRADE NITRILE GLOVES</li>
      </ul>
    </div>

    <div class="price">
      <span class="price__for">FOR</span>
      <span class="price__main">$9.</span>
      <span class="price__cents">99</span>
    </div>

    <div class="case-note">No limit. Each case is $99.</div>

    <div class="closing">
      <p>Sale ends on December 4th.</p>
      <p>Visit: <span class="closing__url">www.kelptorch.com</span></p>
    </div>

    <div class="brand">kelptorch.com</div>
  </section>
</div>
</body>
</html>
```